Harrow Glen Whiskey Label

We are looking for a label to be made for our single batch whiskey. in the attached pdf you will see the lay out of the design. We are going to use a whiskey bottle with a cork. Some of the label you will need to leave some space for hand writing.

Target Market(s)

people who like craft beer and whiskey

Industry/Entity Type

Craft Distillery

Font styles to use
Decorative

Colors

Designer to choose colors to be used in the design.

Requirements
Must have
• room for hand writing informatiom

```html
<!DOCTYPE html>
<html lang="en">
<head>
<meta charset="utf-8">
<title>Harrow Glen Single Batch Whiskey Label</title>
<link href="https://fonts.googleapis.com/css2?family=Cinzel:wght@400;700&family=UnifrakturCook:wght@700&display=swap" rel="stylesheet">
<style>
  :root {
    --backdrop: #f3f3f5;
    --paper: #f4f3f7;
    --paper-shade: #e4e3ea;
    --band: #171728;
    --gold: #b8985a;
    --ink: #2a2a33;
    --rule: #56565f;
    --rule-soft: #9a99a3;
  }
  * { margin: 0; padding: 0; box-sizing: border-box; }
  html, body { width: 900px; height: 1200px; overflow: hidden; background: var(--backdrop); }
  .canvas { position: relative; width: 900px; height: 1200px; }
  .label {
    position: absolute; left: 130px; top: 170px; width: 640px; height: 860px;
    background: linear-gradient(160deg, var(--paper) 0%, var(--paper) 60%, var(--paper-shade) 100%);
    box-shadow: 0 14px 40px rgba(40, 40, 60, 0.18);
    overflow: hidden;
    font-family: "Cinzel", "Times New Roman", serif;
    color: var(--ink);
  }
  .label-art { position: absolute; inset: 0; }
  .brand-mark {
    position: absolute; right: 48px; top: 44px;
    display: flex; align-items: center; gap: 8px;
    font-weight: 700; font-size: 16px; letter-spacing: 2px; color: var(--band);
    white-space: nowrap;
  }
  .brand-mark .dot { width: 14px; height: 14px; border-radius: 50%; background: var(--band); }
  .product-name {
    position: absolute; left: 0; top: 225px; width: 100%;
    text-align: center; transform: rotate(-13deg);
    font-family: "UnifrakturCook", "Old English Text MT", serif; font-weight: 700;
    color: var(--gold); font-size: 66px; line-height: 0.95; letter-spacing: 2px;
  }
  .product-name span { display: block; }
  .product-name .second { padding-left: 40px; }
  .descriptor { position: absolute; left: 70px; top: 488px; }
  .descriptor .style { font-weight: 700; font-size: 17px; letter-spacing: 1px; }
  .descriptor .grain { font-size: 14px; line-height: 1.2; margin-top: 8px; color: #55545e; letter-spacing: 1px; }
  .field {
    position: absolute; font-size: 12px; letter-spacing: 0.5px; color: #4a4952; white-space: nowrap;
  }
  .field-source { left: 86px; top: 580px; }
  .field-aged { left: 86px; top: 652px; }
  .field-bottle { left: 86px; top: 722px; }
  .field-abv { left: 412px; top: 566px; }
  .field-of { left: 420px; top: 652px; }
  .producer {
    position: absolute; right: 46px; bottom: 34px; text-align: right;
    font-size: 12px; line-height: 1.35; letter-spacing: 0.5px; color: #3e3d47;
  }
  .volume { margin-top: 10px; font-size: 15px; }
</style>
</head>
<body>
<div class="canvas">
  <section class="label">
    <svg class="label-art" width="640" height="860" viewBox="0 0 640 860" aria-hidden="true">
      <path class="title-band" d="M0 300 Q 300 200 640 110 L 640 300 Q 320 380 0 470 Z" fill="var(--band)"/>
      <path class="accent-arc" d="M385 478 Q 350 525 385 575" fill="none" stroke="var(--rule-soft)" stroke-width="1.2"/>
      <path class="accent-gold" d="M395 525 Q 480 480 560 415" fill="none" stroke="var(--gold)" stroke-width="2"/>
      <g class="write-lines" stroke="var(--rule)" stroke-width="1" fill="none">
        <line x1="80" y1="622" x2="360" y2="584"/>
        <line x1="80" y1="694" x2="360" y2="658"/>
        <line x1="80" y1="764" x2="320" y2="734"/>
        <line x1="412" y1="610" x2="600" y2="495"/>
        <line x1="450" y1="684" x2="600" y2="590"/>
      </g>
    </svg>

    <div class="brand-mark"><span class="dot"></span>IRON SPUR</div>

    <h1 class="product-name"><span>Harrow</span><span class="second">Glen</span></h1>

    <div class="descriptor">
      <p class="style">SINGLE BATCH WHISKEY</p>
      <p class="grain">SPIRITS DISTILLED FROM<br>MALT MASH AND HOPS</p>
    </div>

    <p class="field field-source">DISTILLATE SOURCE:</p>
    <p class="field field-aged">AGED:</p>
    <p class="field field-bottle">BOTTLE:</p>
    <p class="field field-abv">% ALC. BY VOL</p>
    <p class="field field-of">OF</p>

    <div class="producer">
      <p>DISTILLED AND BOTTLED BY<br>IRON SPUR DISTILLERY LLC<br>48 FOUNDRY LANE, MILLBROOK NJ 08321</p>
      <p class="volume">750ML</p>
    </div>
  </section>
</div>
</body>
</html>
```